KRV Inc Web Design

WHAT ARE WE DOING?
We are developing a new website look and feel for a new company called KRV Inc. This new look and feel should include colors, design elements, choice of photography and other imagery, fonts, and other user experience elements.

WHAT DO THEY DO?
KRV, Inc, makes tools for researchers who are studying protein-protein interactions. These molecules are the basic tools of biology, and serve as key targets for drug developers and disease researchers. The world of proteins is enormously complex, and companies like KRV provide researchers with critical tools that help them elucidate this world.

WHO ARE WE TALKING TO?
The target audience for this website are professional scientists working in university research or biopharma drug development. They are highly sophisticated consumers looking for key tools that will advance their research.

WHAT DO WE WANT THEM TO DO?
The site is an information resource for the customer exploring the tools that KRV sells and the scientific issues surrounding protein-protein interactions. They should be able to navigate easily to their content of choice, while the whole site should convey a professionalism that enhanced KRV’s credibility.

WHAT DOES THE KRV BRAND STAND FOR?
KRV stands for illumination. Proteins are challenging to study, and KRV exists to help shed light on their workings.

WHAT ARE THE KEY VALUES OF THE KRV BRAND?
Integrity. Innovation. Insight.

WHAT ARE THE EXECUTIONAL MANDITORIES?
The look and feel is completely up for grabs. Nothing is off the table.

WHAT ARE THE DELIVERABLES?
We need new designs for the following templates:
http://cms.thevormelgroup.com/
http://cms.thevormelgroup.com/products-and-services/instruments-3/bench-top-instruments/
http://cms.thevormelgroup.com/category/lab-study/

```html
<!DOCTYPE html>
<html lang="en">
<head>
<meta charset="utf-8">
<title>KRV Inc</title>
<link href="https://fonts.googleapis.com/css2?family=Roboto:wght@300;400&display=swap" rel="stylesheet">
<style>
:root{
  --accent:#f9ae3d;
  --text:#777;
  --heading:#444;
  --nav:#999;
  --footer:#3d3d3d;
  --white:#fff;
  --dot:#444;
}
*{margin:0;padding:0;box-sizing:border-box}
html,body{width:1200px;height:1065px;overflow:hidden;background:var(--white);font-family:'Roboto',sans-serif}
body{position:relative}
.site-header{position:relative;height:111px}
.brand{position:absolute;left:130px;top:38px;font-size:40px;font-weight:300;letter-spacing:6px;color:#666;line-height:48px}
.search{position:absolute;left:879px;top:8px;width:178px;height:28px;border:1px solid #ddd;font-size:11px;color:#999;padding:7px 9px}
.search svg{position:absolute;right:4px;top:6px}
.main-nav{position:absolute;right:141px;top:50px;font-size:18px;font-weight:300;color:var(--nav)}
.main-nav a{color:var(--nav);text-decoration:none}
.main-nav a.active{color:var(--accent)}
.hero{position:relative;height:509px;background:linear-gradient(100deg,#c9dbe6 0%,#8fb8d3 30%,#e7eef2 55%,#f3f3f1 75%,#8a7a6c 100%)}
.hero-dots{position:absolute;left:557px;top:455px;display:flex;gap:5px}
.hero-dots span{width:18px;height:18px;border-radius:50%;background:var(--dot)}
.hero-dots span:first-child{background:var(--accent)}
.values{position:relative;height:332px}
.value{position:absolute;top:42px;width:300px;text-align:center}
.value h2{font-size:24px;font-weight:300;color:var(--heading);display:flex;align-items:center;justify-content:center;gap:14px;height:50px;margin-bottom:8px}
.value p{font-size:12px;font-weight:300;line-height:24px;letter-spacing:-0.3px;color:var(--text);text-align:justify;text-align-last:center}
.btn{display:inline-block;width:118px;height:38px;line-height:38px;background:var(--accent);color:var(--white);font-size:14px;margin-top:16px;text-decoration:none}
.site-footer{position:absolute;top:952px;left:0;width:1200px;height:113px;background:var(--footer);color:var(--white);font-size:14px}
.footer-nav{position:absolute;left:130px;top:29px}
.copyright{position:absolute;left:130px;top:67px}
.social{position:absolute;left:992px;top:41px;display:flex;gap:6px}
.social span{width:36px;height:36px;border-radius:50%}
</style>
</head>
<body>
<header class="site-header">
  <div class="brand">KRV INC</div>
  <div class="search">Search
    <svg width="14" height="14" viewBox="0 0 14 14"><circle cx="5.5" cy="5.5" r="4" fill="none" stroke="#555" stroke-width="1.5"/><line x1="8.5" y1="8.5" x2="13" y2="13" stroke="#555" stroke-width="2"/></svg>
  </div>
  <nav class="main-nav"><a class="active" href="#">Company</a> | <a href="#">Products &amp; Services</a> | <a href="#">Learning Center</a> | <a href="#">Events</a> | <a href="#">KRV News</a> | <a href="#">Contact Us</a></nav>
</header>
<section class="hero" role="img" aria-label="Scientists in a laboratory working with a microscope and a flask of blue liquid">
  <div class="hero-dots"><span></span><span></span><span></span><span></span></div>
</section>
<section class="values">
  <div class="value" style="left:130px">
    <h2><svg width="24" height="36" viewBox="0 0 24 36"><circle cx="12" cy="3" r="1.5" fill="#f9ae3d"/><circle cx="9" cy="7" r="1.2" fill="#f9ae3d"/><path d="M8 12h8v8l7 13H1l7-13z" fill="none" stroke="#f9ae3d" stroke-width="2"/><path d="M4 27h16l2 5H2z" fill="#f9ae3d"/></svg>Integrity</h2>
    <p>Lorem Ipsum is simply dummy text of the printing and typesetting industry. Lorem Ipsum has been the industry's standard dummy text ever since the 1500s, when an unknown printer took a galley of type and scrambled it to make a type specimen book. It has survived</p>
    <a class="btn" href="#" style="margin-left:-2px">Read More</a>
  </div>
  <div class="value" style="left:453px">
    <h2><svg width="18" height="32" viewBox="0 0 18 32"><path d="M9 1a8 8 0 0 0-5 14v5h10v-5A8 8 0 0 0 9 1z" fill="#f9ae3d"/><rect x="5" y="22" width="8" height="2" fill="#f9ae3d"/><rect x="6" y="26" width="6" height="2" fill="#f9ae3d"/></svg>Innovation</h2>
    <p>Lorem Ipsum is simply dummy text of the printing and typesetting industry. Lorem Ipsum has been the industry's standard dummy text ever since the 1500s, when an unknown printer took a galley of type and scrambled it to make a type specimen book. It has survived</p>
    <a class="btn" href="#" style="margin-left:18px">Read More</a>
  </div>
  <div class="value" style="left:772px">
    <h2><svg width="32" height="26" viewBox="0 0 32 26"><path d="M2 9h6l14-8v24L8 17H2z" fill="#f9ae3d"/><rect x="8" y="17" width="4" height="8" fill="#f9ae3d"/><path d="M25 8l5-3M25 13h6M25 18l5 3" stroke="#f9ae3d" stroke-width="2"/></svg>Insight</h2>
    <p>Lorem Ipsum is simply dummy text of the printing and typesetting industry. Lorem Ipsum has been the industry's standard dummy text ever since the 1500s, when an unknown printer took a galley of type and scrambled it to make a type specimen book. It has survived</p>
    <a class="btn" href="#" style="margin-left:12px">Read More</a>
  </div>
</section>
<footer class="site-footer">
  <div class="footer-nav">Company | Products &amp; Services | Learning Center | Events | KRV News | Contact Us</div>
  <div class="copyright">Copyright ©2013 &nbsp;Company Name &nbsp;&nbsp;&nbsp;- All rights reserved</div>
  <div class="social"><span style="background:#5bb8e8"></span><span style="background:#4a6db0"></span></div>
</footer>
</body>
</html>
```